Sales Brochure

Industrial brochure of my industrial pump business which includes repair and sales of equipment. I distribute and repair industrial pumps for the midwest market. Design color is blue.

```html
<!DOCTYPE html>
<html lang="en">
<head>
<meta charset="UTF-8">
<title>Pump Sales &amp; Repair Brochure</title>
<link href="https://fonts.googleapis.com/css2?family=Poppins:wght@400;500;600;700&family=Roboto+Condensed:wght@700;800&display=swap" rel="stylesheet">
<style>
  :root{
    --bg:#e4e4e4;
    --paper:#f7f8f9;
    --blue:#2f6fdc;
    --blue-deep:#1f52d6;
    --sky:#a9cbe6;
    --ink:#1c1c1c;
    --text:#4a4a4a;
  }
  *{margin:0;padding:0;box-sizing:border-box}
  html,body{width:802px;height:1200px;overflow:hidden}
  body{background:var(--bg);font-family:"Poppins",sans-serif;position:relative}

  .spread{position:absolute;left:21px;width:760px;height:537px;background:var(--paper);box-shadow:0 6px 18px rgba(0,0,0,.12)}
  .spread--outside{top:40px}
  .spread--inside{top:623px}
  .spread__art{position:absolute;inset:0}
  .fold{position:absolute;left:380px;top:0;width:1px;height:100%;background:rgba(0,0,0,.06)}

  /* outside */
  .cover-title{position:absolute;right:30px;top:350px;text-align:right;font-family:"Roboto Condensed",sans-serif;font-weight:800;color:var(--blue-deep);line-height:1.05}
  .cover-title__main{display:block;font-size:27px}
  .cover-title__sub{display:block;font-size:19px}
  .contact{position:absolute;left:30px;top:440px;font-family:"Roboto Condensed",sans-serif;font-weight:700;color:var(--blue-deep)}
  .contact__label{display:inline-block;background:var(--blue);color:#fff;font-size:20px;padding:3px 12px;margin-bottom:6px}
  .contact__line{font-size:13px;line-height:1.3}

  /* inside */
  .page{position:absolute;top:0;width:380px;height:537px}
  .page--left{left:0;padding:22px 22px 0 24px}
  .page--right{left:380px;padding:30px 24px 0 22px}
  .heading{font-size:10px;font-weight:700;color:var(--ink);text-transform:uppercase;border-bottom:1px solid var(--ink);display:inline-block;padding-bottom:1px;margin-bottom:4px;letter-spacing:.2px}
  .heading--sm{font-size:8.5px}
  .body{font-size:6.6px;line-height:1.45;color:var(--text);margin-bottom:9px}
  .caps{text-transform:uppercase;font-size:6px}
  .pump-row{display:flex;gap:8px;margin:4px 0 10px}
  .pump{width:74px}
  .pump__photo{display:block;width:74px;height:50px;background:linear-gradient(135deg,#28456f,#6d8fb8 55%,#c9d3de)}
  .pump__name{font-size:5.8px;font-weight:600;color:var(--ink);text-transform:uppercase;text-align:center;margin-top:3px;line-height:1.2}
  .repair{display:flex;gap:14px;margin-top:4px}
  .repair__photos{display:flex;flex-direction:column;gap:6px}
  .repair__photo{display:block;width:120px;height:82px}
  .repair__photo--gear{background:linear-gradient(135deg,#2b2b2b,#8a8a8a 60%,#c8c8c8)}
  .repair__photo--pipe{background:linear-gradient(135deg,#2c6fd6,#9fb6cf 50%,#e1e8f0)}
  .repair__text{flex:1;padding-top:10px}
  .bullets{list-style:disc;padding-left:10px;margin-bottom:10px}
  .bullets li{font-size:6.6px;line-height:1.45;color:var(--text);margin-bottom:2px}
  .bullets b{font-weight:600;color:var(--ink)}
  .page__art{position:absolute;left:0;top:0}
</style>
</head>
<body>

<section class="spread spread--outside" aria-label="Brochure outside spread">
  <svg class="spread__art" width="760" height="537" viewBox="0 0 760 537">
    <defs>
      <linearGradient id="skyFade" x1="0" y1="0" x2="1" y2="0">
        <stop offset="0.15" stop-color="#ffffff"/>
        <stop offset="0.5" stop-color="#d3e3f0"/>
        <stop offset="1" stop-color="var(--sky)"/>
      </linearGradient>
      <linearGradient id="plantTones" x1="0" y1="0" x2="0" y2="1">
        <stop offset="0" stop-color="#7fb1e0"/>
        <stop offset="0.45" stop-color="#c8b45a"/>
        <stop offset="0.75" stop-color="#b9bec4"/>
        <stop offset="1" stop-color="#8d949b"/>
      </linearGradient>
      <clipPath id="upperArea">
        <path d="M110,0 C180,300 520,360 760,250 L760,0 Z"/>
      </clipPath>
    </defs>
    <path d="M110,0 C180,300 520,360 760,250 L760,0 Z" fill="url(#skyFade)"/>
    <g clip-path="url(#upperArea)">
      <rect x="380" y="0" width="380" height="340" fill="url(#plantTones)" role="img" aria-label="Photo of an industrial pumping station with yellow and grey pipework under a blue sky"/>
    </g>
    <path d="M104,-10 C178,306 520,370 770,258" fill="none" stroke="var(--blue)" stroke-width="26"/>
    <path d="M-10,398 C140,358 300,362 410,445" fill="none" stroke="var(--blue)" stroke-width="24"/>
  </svg>
  <div class="fold"></div>

  <h1 class="cover-title">
    <span class="cover-title__main">YOUR TRUSTED PARTNER</span>
    <span class="cover-title__sub">FOR PUMP SALES AND REPAIR</span>
  </h1>

  <div class="contact">
    <div class="contact__label">CONTACT US</div>
    <div class="contact__line">00551234987</div>
    <div class="contact__line">WWW.PRAIRIEFLOWPUMPS.COM</div>
  </div>
</section>

<section class="spread spread--inside" aria-label="Brochure inside spread">
  <div class="page page--left">
    <h2 class="heading">About Us</h2>
    <p class="body">At [Your Company Name], we specialize in providing top-quality industrial pumps and comprehensive repair services for the Midwest market. With years of experience and a commitment to excellence, we ensure that your operations run smoothly and efficiently.</p>

    <h2 class="heading">Our Services :</h2>
    <h3 class="heading heading--sm">Wide Selection</h3>
    <p class="body caps" style="margin-bottom:2px">We offer a diverse range of industrial pumps suitable for various applications, including:</p>
    <div class="pump-row">
      <div class="pump"><span class="pump__photo" role="img" aria-label="Photo of centrifugal pumps"></span><p class="pump__name">Centrifugal Pumps</p></div>
      <div class="pump"><span class="pump__photo" role="img" aria-label="Photo of positive displacement pumps"></span><p class="pump__name">Positive Displacement Pumps</p></div>
      <div class="pump"><span class="pump__photo" role="img" aria-label="Photo of submersible pumps"></span><p class="pump__name">Submersible Pumps</p></div>
      <div class="pump"><span class="pump__photo" role="img" aria-label="Photo of specialty pumps"></span><p class="pump__name">Specialty Pumps</p></div>
    </div>

    <h3 class="heading heading--sm">Expert Consultation</h3>
    <p class="body">Our knowledgeable team assists you in selecting the right pump for your specific needs, ensuring optimal performance and reliability.</p>

    <h2 class="heading">Repair and Maintenance</h2>
    <div class="repair">
      <div class="repair__photos">
        <span class="repair__photo repair__photo--gear" role="img" aria-label="Photo of a pump gear assembly under repair"></span>
        <span class="repair__photo repair__photo--pipe" role="img" aria-label="Photo of blue industrial pump pipework"></span>
      </div>
      <div class="repair__text">
        <h3 class="heading heading--sm">Comprehensive Repair Services</h3>
        <p class="body">Our skilled technicians provide efficient repair solutions to minimize downtime and extend the life of your equipment.</p>
        <h3 class="heading heading--sm">Preventive Maintenance Plans</h3>
        <p class="body">Tailored maintenance programs designed to keep your pumps operating at peak efficiency.</p>
      </div>
    </div>
  </div>

  <div class="page page--right">
    <svg class="page__art" width="380" height="537" viewBox="0 0 380 537">
      <defs>
        <linearGradient id="stationTones" x1="0" y1="0" x2="1" y2="1">
          <stop offset="0" stop-color="#3a3d44"/>
          <stop offset="0.5" stop-color="#b8bcc2"/>
          <stop offset="0.8" stop-color="#c63a3a"/>
          <stop offset="1" stop-color="#9aa0a6"/>
        </linearGradient>
      </defs>
      <circle cx="62" cy="316" r="24" fill="var(--blue)"/>
      <path d="M0,392 C70,320 210,318 380,292 L380,537 L0,537 Z" fill="var(--blue)"/>
      <path d="M0,412 C70,342 210,338 380,314 L380,537 L0,537 Z" fill="url(#stationTones)" role="img" aria-label="Photo of a technician in a hard hat beside booster pumps and red pressure tanks"/>
    </svg>
    <div style="position:relative">
      <h2 class="heading">Why Choose Us?</h2>
      <ul class="bullets">
        <li><b>Quality Products:</b> We source only the best pumps from trusted manufacturers.</li>
        <li><b>Expertise:</b> Our team has extensive industry knowledge and hands-on experience.</li>
        <li><b>Customer-Centric Approach:</b> We prioritize your needs and work to provide tailored solutions.</li>
        <li><b>Fast Turnaround:</b> We understand the urgency of industrial operations and strive to deliver prompt service.</li>
      </ul>
      <h2 class="heading">Our Commitment</h2>
      <p class="body">At [Your Company Name], we are dedicated to delivering superior products and services. Our mission is to enhance your operations with reliable pump solutions and exceptional customer service.</p>
    </div>
  </div>
  <div class="fold"></div>
</section>

</body>
</html>
```